Graphic Design for a Info Card

We would like a graphic design for an info card . We would like the colours to correspond to our logo , you can add in the colours navy blue or yellow if you would like. We would like it to have the following information. We want something that really pops. We would like the size to be 4 1/2 x 6 .

ATTENTION!! Delivery Promo! Order from us on the @hopmorsel app or @vantrelcourier app on FRIDAYS and receive a FREE Sample of our one of our meal prep meals in your bag!
DID YOU KNOW?! Meal Prep is another great service that we offer. Saving you time, promoting your health, and best of all providing a delicious lunch . You can find more info on our website www.marlowpantry.example . All orders are available for delivery or pickup!

```html
<!DOCTYPE html>
<html lang="en">
<head>
<meta charset="utf-8">
<title>Marlow Healthy Kitchen – Info Card</title>
<link rel="stylesheet" href="https://fonts.googleapis.com/css2?family=Syncopate:wght@700&family=Poppins:wght@400;600&family=Archivo:wght@800&display=swap">
<style>
  :root {
    --stage: #cbcbcb;
    --lime-light: #b6d64f;
    --lime: #8cc42c;
    --lime-deep: #5f9a1c;
    --navy: #10254f;
    --ink: #1b1b1b;
    --white: #ffffff;
    --wood: #8a7b62;
    --wood-dark: #5c4f3c;
  }
  * { margin: 0; padding: 0; box-sizing: border-box; }
  html, body { width: 1200px; height: 1200px; overflow: hidden; }
  body { background: var(--stage); position: relative; font-family: "Poppins", sans-serif; }

  .card {
    position: absolute; top: 240px; width: 510px; height: 679px; overflow: hidden;
    background: radial-gradient(ellipse at 50% 40%, var(--lime-light) 0%, var(--lime) 55%, var(--lime-deep) 100%);
  }
  .card--promo { left: 51px; }
  .card--info  { left: 603px; }

  .line { position: absolute; left: 0; right: 0; text-align: center; white-space: nowrap; }
  .caps { font-family: "Syncopate", sans-serif; font-weight: 700; }

  .rule { position: absolute; height: 2px; background: var(--navy); opacity: .75; }

  /* promo card */
  .promo-title { top: 108px; font-size: 46px; line-height: 56px; color: var(--navy); letter-spacing: 1px; }
  .promo-sub   { top: 156px; font-size: 22px; line-height: 28px; color: var(--navy); }
  .promo-body  { font-size: 18px; line-height: 28px; color: var(--navy); }
  .promo-free  { font-size: 25px; line-height: 34px; color: var(--navy); }
  .promo-free b { font-weight: 400; color: #123f7a; }

  .promo-photo {
    position: absolute; left: 0; right: 0; bottom: 0; height: 240px;
    background: linear-gradient(180deg, rgba(138,123,98,0) 0%, var(--wood) 30%, var(--wood-dark) 100%);
  }

  .brand-name { font-family: "Archivo", sans-serif; font-weight: 800; letter-spacing: 2px; }
  .brand-tag  { font-family: "Archivo", sans-serif; font-weight: 800; }
  .promo-brand { top: 480px; font-size: 46px; line-height: 54px; color: var(--white); }
  .promo-tag   { top: 528px; font-size: 14px; line-height: 20px; color: var(--lime-light); }

  /* info card */
  .info-art {
    position: absolute; left: 0; right: 0; bottom: 0; height: 330px;
    background: linear-gradient(180deg, rgba(140,196,44,0) 0%, rgba(110,176,40,.55) 50%, rgba(96,160,32,.7) 100%);
  }
  .info-title { top: 84px; font-size: 40px; line-height: 50px; color: var(--ink); }
  .info-lead  { top: 143px; font-size: 16px; line-height: 24px; font-weight: 600; color: var(--ink); }
  .info-point { font-size: 14px; line-height: 20px; color: var(--navy); letter-spacing: 1px; }
  .info-web   { top: 294px; font-size: 15px; line-height: 22px; color: var(--navy); }

  .web-pill {
    position: absolute; top: 324px; left: 134px; width: 236px; height: 23px;
    background: var(--white); border-radius: 12px; display: flex; align-items: center;
    box-shadow: 0 3px 4px rgba(0,0,0,.25);
  }
  .web-pill__icon {
    width: 36px; height: 23px; background: var(--navy); border-radius: 12px 0 0 12px;
    display: flex; align-items: center; justify-content: center;
  }
  .web-pill__url { flex: 1; text-align: center; font-size: 12px; font-weight: 600; color: var(--navy); }

  .info-note  { font-size: 14px; line-height: 20px; color: var(--navy); letter-spacing: 1px; }
  .info-brand { top: 552px; font-size: 46px; line-height: 54px; color: var(--ink); }
  .info-tag   { top: 602px; font-size: 15px; line-height: 20px; color: var(--ink); }
</style>
</head>
<body>

<section class="card card--promo">
  <div class="promo-photo" role="img" aria-label="Photo of fresh vegetables and fruit in a heart-shaped bowl on a wooden table"></div>

  <h1 class="line caps promo-title">ATTENTION!!</h1>
  <h2 class="line caps promo-sub">Delivery Promo!</h2>
  <div class="rule" style="top:199px; left:69px; width:362px;"></div>

  <p class="line promo-body" style="top:224px;">Order from us on the</p>
  <p class="line promo-body" style="top:260px;">@hopmorsel app or @vantrelcourier app</p>
  <p class="line promo-body" style="top:294px;">on FRIDAYS andreceive a</p>
  <p class="line promo-free" style="top:326px;"><b>FREE</b> Sample</p>
  <p class="line promo-body" style="top:364px;">of our one of our meal prep</p>
  <p class="line promo-body" style="top:399px;">meals in your bag!</p>

  <p class="line brand-name promo-brand">MARLOW</p>
  <p class="line brand-tag promo-tag">HEALTHY KITCHEN&nbsp;&nbsp;|&nbsp;&nbsp;MEAL PREP</p>
</section>

<section class="card card--info">
  <div class="info-art" role="img" aria-label="Faint line drawings of vegetables, herbs and fruit"></div>

  <h1 class="line caps info-title">DID YOU KNOW?</h1>
  <p class="line info-lead">Meal Prep is another great service that we offer.</p>

  <p class="line caps info-point" style="top:178px;">Saving you time,</p>
  <div class="rule" style="top:202px; left:73px; width:364px;"></div>
  <p class="line caps info-point" style="top:204px;">promoting your health,</p>
  <div class="rule" style="top:228px; left:73px; width:364px;"></div>
  <p class="line caps info-point" style="top:230px;">and best of all providing a</p>
  <p class="line caps info-point" style="top:252px;">delicious lunch</p>
  <div class="rule" style="top:274px; left:73px; width:364px;"></div>

  <p class="line info-web">You can find more info on our website</p>
  <div class="web-pill">
    <span class="web-pill__icon">
      <svg width="15" height="15" viewBox="0 0 16 16" fill="none" stroke="#ffffff" stroke-width="1.2">
        <circle cx="8" cy="8" r="7"/>
        <ellipse cx="8" cy="8" rx="3" ry="7"/>
        <line x1="1" y1="8" x2="15" y2="8"/>
        <line x1="2.2" y1="4.5" x2="13.8" y2="4.5"/>
        <line x1="2.2" y1="11.5" x2="13.8" y2="11.5"/>
      </svg>
    </span>
    <span class="web-pill__url">www.marlowpantry.example</span>
  </div>

  <p class="line caps info-note" style="top:362px;">All orders are available</p>
  <p class="line caps info-note" style="top:386px;">for delivery or pickup!</p>

  <p class="line brand-name info-brand">MARLOW</p>
  <p class="line brand-tag info-tag">HEALTHY KITCHEN&nbsp;&nbsp;|&nbsp;&nbsp;MEAL PREP</p>
</section>

</body>
</html>
```